Website Design for Law Firm

We need a fresh new website design for our client 'Torvek Legal' who specialises as a Criminal, Traffic & Civil Lawyer in Perth, Western Australia. We are looking for a very clean, professional and elegant look for the website, a presence of power and class needed as he deals with high end clients. Black, Silver and hints of gold need to run through the design without making the site look too dark. We are after a very modern, spacious web look, use of large readable text with links to social media (such as Facebook, Google+, Twitter, LinkedIn) to stand out and his contact details to be made very predominate.

Reason: Public holidays here in Australia, need more business hours to discuss designs with client.

Reason: Client needs more time to look through designs.

Reason: Client is going over last of designs. Design will be picked early next week!

Law Firm

```html
<!DOCTYPE html>
<html lang="en">
<head>
<meta charset="utf-8">
<title>Torvek Legal — Criminal, Traffic &amp; Civil Lawyer</title>
<link href="https://fonts.googleapis.com/css2?family=Open+Sans:wght@300;400;600;700&family=Bitter:wght@400;700&display=swap" rel="stylesheet">
<style>
  :root {
    --ink: #2b2b2b;
    --heading: #5c5c5c;
    --text: #777777;
    --gold: #e0b400;
    --gold-soft: #d9c34a;
    --band: #f4f4f4;
    --panel: #efefef;
    --rule: #dddddd;
    --footer: #3a3a3a;
    --footer-text: #e6e6e6;
    --footer-muted: #bdbdbd;
    --black: #1f1f1f;
    --white: #ffffff;
    --social-active: #55acee;
  }
  * { box-sizing: border-box; margin: 0; padding: 0; }
  html, body { width: 787px; height: 1200px; overflow: hidden; }
  body {
    position: relative;
    background: var(--white);
    font-family: "Open Sans", Arial, sans-serif;
    color: var(--text);
  }
  a { color: inherit; text-decoration: none; }

  /* Header */
  .site-header { position: absolute; top: 0; left: 0; width: 787px; height: 86px; }
  .brand {
    position: absolute; left: 77px; top: 36px;
    display: flex; align-items: center; gap: 8px;
    font-weight: 700; font-size: 24px; letter-spacing: 0.5px;
    color: var(--ink); text-transform: uppercase;
  }
  .brand-mark { width: 14px; height: 14px; background: var(--ink); }
  .phone-box {
    position: absolute; left: 548px; top: 0; width: 160px; height: 34px;
    background: var(--panel);
    display: flex; align-items: center; justify-content: center; gap: 7px;
    font-family: "Bitter", Georgia, serif; font-size: 11.5px; color: #555;
  }
  .phone-box strong { font-family: "Open Sans", Arial, sans-serif; font-weight: 700; font-size: 12px; color: #444; letter-spacing: 0.3px; }
  .main-nav {
    position: absolute; right: 81px; top: 67px;
    display: flex; gap: 24px;
    font-family: "Bitter", Georgia, serif; font-size: 11.5px; color: #555;
  }
  .main-nav .current { color: var(--gold); }

  /* Hero */
  .hero { position: absolute; left: 0; top: 86px; width: 787px; height: 271px; overflow: hidden; }
  .hero-photo {
    position: absolute; inset: 0;
    background:
      radial-gradient(ellipse at 20% 60%, rgba(90,100,80,0.55), transparent 45%),
      radial-gradient(ellipse at 75% 70%, rgba(150,140,130,0.45), transparent 50%),
      linear-gradient(180deg, #3e3e3e 0%, #2c2c2c 45%, #4a4a48 100%);
  }
  .hero-content { position: absolute; inset: 0; text-align: center; }
  .hero-title {
    position: absolute; top: 102px; width: 100%;
    font-weight: 300; font-size: 26px; color: #f0f0f0; letter-spacing: -0.3px;
  }
  .hero-tagline {
    position: absolute; top: 138px; width: 100%;
    font-family: Arial, Helvetica, sans-serif; font-size: 9px; color: var(--gold);
  }
  .hero-cta {
    position: absolute; left: 316px; top: 168px; width: 153px; height: 26px;
    border-radius: 13px; background: rgba(70,70,70,0.85);
    display: flex; align-items: center; justify-content: center; gap: 5px;
    font-family: Arial, Helvetica, sans-serif; font-size: 10.5px; color: var(--white); letter-spacing: 0.3px;
  }
  .hero-cta svg { width: 12px; height: 6px; }

  /* About + News */
  .section-title {
    font-weight: 700; font-size: 16px; color: var(--heading);
    text-transform: uppercase; letter-spacing: 0.2px;
  }
  .about { position: absolute; left: 79px; top: 393px; width: 400px; }
  .about p { margin-top: 18px; font-size: 8.1px; line-height: 11.9px; color: var(--text); white-space: nowrap; }
  .btn-dark {
    display: inline-flex; align-items: center; justify-content: center;
    margin-top: 11px; width: 88px; height: 22px;
    background: var(--black); color: var(--white); font-size: 9.5px; font-weight: 600;
  }
  .news { position: absolute; left: 497px; top: 393px; width: 211px; }
  .news-list { margin-top: 8px; background: var(--panel); padding: 0 9px 14px; list-style: none; }
  .news-list li {
    display: flex; justify-content: space-between; align-items: center;
    height: 25.5px; border-bottom: 1px solid var(--rule);
    font-family: Arial, Helvetica, sans-serif; font-size: 7.3px; color: #444;
  }
  .news-list li:last-child { border-bottom: none; }
  .news-list svg { width: 10px; height: 5px; }

  /* Services */
  .services { position: absolute; left: 0; top: 632px; width: 787px; height: 251px; background: var(--band); }
  .services-title { position: absolute; top: 26px; width: 100%; text-align: center; }
  .services-rule { position: absolute; left: 292px; top: 46px; width: 196px; height: 1px; background: var(--gold-soft); }
  .service { position: absolute; top: 94px; width: 150px; text-align: center; }
  .service h3 { font-family: "Bitter", Georgia, serif; font-weight: 700; font-size: 11.5px; color: #444; letter-spacing: 0.6px; }
  .service svg { display: block; margin: 9px auto 0; height: 40px; }
  .service p { margin-top: 14px; font-family: Arial, Helvetica, sans-serif; font-size: 7.2px; line-height: 9.3px; color: #777; }

  /* Social */
  .social { position: absolute; left: 0; top: 928px; width: 787px; height: 38px; }
  .social a {
    position: absolute; top: 0; width: 38px; height: 38px;
    border: 2px solid var(--gold); background: #e4e4e4;
    display: flex; align-items: center; justify-content: center;
  }
  .social a.white { background: var(--white); }
  .social a.active { border: none; background: var(--social-active); }
  .social .dot { width: 7px; height: 7px; border-radius: 50%; background: #444; }
  .social a.active .dot { background: var(--white); }

  /* Footer */
  .site-footer { position: absolute; left: 0; top: 1018px; width: 787px; height: 182px; background: var(--footer); color: var(--footer-text); }
  .footer-col { position: absolute; top: 50px; }
  .footer-col h4 { font-weight: 600; font-size: 10px; color: var(--white); }
  .footer-col ul { list-style: none; margin-top: 11px; }
  .footer-col li { font-family: Arial, Helvetica, sans-serif; font-size: 7.5px; line-height: 15.7px; color: var(--footer-text); }
  .footer-col address { font-style: normal; margin-top: 12px; font-family: Arial, Helvetica, sans-serif; font-size: 7.5px; line-height: 13px; font-weight: 700; color: var(--footer-text); }
  .footer-col .muted { font-weight: 400; color: var(--footer-muted); }
  .map-line { margin-top: 2px; font-family: Arial, Helvetica, sans-serif; font-size: 7.5px; color: var(--footer-muted); }
  .map-link { text-decoration: underline; }
  .footer-col .about-text { margin-top: 12px; width: 145px; font-family: Arial, Helvetica, sans-serif; font-weight: 700; font-size: 7.5px; line-height: 13px; color: var(--footer-text); }
</style>
</head>
<body>

<header class="site-header">
  <a class="brand" href="#"><span class="brand-mark"></span>Torvek Legal</a>
  <div class="phone-box">Tepehone: <strong>123-555-0174</strong></div>
  <nav class="main-nav">
    <a class="current" href="#">Home</a>
    <a href="#">Services</a>
    <a href="#">Our Stories</a>
    <a href="#">News</a>
    <a href="#">Contact</a>
  </nav>
</header>

<section class="hero">
  <div class="hero-photo" role="img" aria-label="Dark desk scene with a potted plant and a hand writing with a pen on paper"></div>
  <div class="hero-content">
    <h1 class="hero-title">Criminal , Traffic &amp; Civil Lawyer</h1>
    <p class="hero-tagline">excepteur sint occaecat cupidatat non proident</p>
    <a class="hero-cta" href="#">CONTACT
      <svg viewBox="0 0 12 6"><path d="M0 3h10M8 1l2 2-2 2" stroke="#e0b400" stroke-width="1.2" fill="none"/></svg>
    </a>
  </div>
</section>

<section class="about">
  <h2 class="section-title">About Torvek Legal</h2>
  <p>Excepteur sint occaecat cupidatat non proident, sunt in culpa qui officia<br>
  deserunt mollit anim id est laborum. Lorem Ipsum is simply dummy text of the printing and type-<br>
  setting industry. Lorem Ipsum has been the industry's standard dummy text ever since the 1500s,<br>
  when an unknown printer took a galley of type and scrambled it to make a type specimen book. It<br>
  has survived not only five centuries, but also the leap into electronic typesetting, remaining es-<br>
  sentially unchanged. It was popularised in the 1960s with the release of Velmaset sheets contain-<br>
  ing Lorem Ipsum passages, and more recently with desktop publishing software like Orin Page-<br>
  Setter including versions of Lorem Ipsum.</p>
  <a class="btn-dark" href="#">Learn More</a>
</section>

<aside class="news">
  <h2 class="section-title">Latest News</h2>
  <ul class="news-list">
    <li>14/10 Lorem Ipsum is dummy text <svg viewBox="0 0 10 5"><path d="M0 2.5h9M7 .8l2 1.7-2 1.7" stroke="#e0b400" fill="none"/></svg></li>
    <li>14/10 Lorem Ipsum is dummy text <svg viewBox="0 0 10 5"><path d="M0 2.5h9M7 .8l2 1.7-2 1.7" stroke="#e0b400" fill="none"/></svg></li>
    <li>14/10 Lorem Ipsum is dummy text <svg viewBox="0 0 10 5"><path d="M0 2.5h9M7 .8l2 1.7-2 1.7" stroke="#e0b400" fill="none"/></svg></li>
    <li>14/10 Lorem Ipsum is dummy text <svg viewBox="0 0 10 5"><path d="M0 2.5h9M7 .8l2 1.7-2 1.7" stroke="#e0b400" fill="none"/></svg></li>
    <li>14/10 Lorem Ipsum is dummy text <svg viewBox="0 0 10 5"><path d="M0 2.5h9M7 .8l2 1.7-2 1.7" stroke="#e0b400" fill="none"/></svg></li>
  </ul>
</aside>

<section class="services">
  <h2 class="section-title services-title">Services</h2>
  <div class="services-rule"></div>

  <article class="service" style="left:77px">
    <h3>DUIS AUTE IRURE</h3>
    <svg viewBox="0 0 32 40" width="32" fill="none" stroke="#444" stroke-width="2">
      <rect x="2" y="5" width="28" height="33"/><rect x="10" y="2" width="12" height="6" fill="#f4f4f4"/>
      <path d="M8 16h16M8 22h16M8 28h16"/>
    </svg>
    <p>Excepteur sint occaecat cupi datat non it proident, sunt in culpa qui officia dese runtorn mollit anim id est laborum.</p>
  </article>

  <article class="service" style="left:236px">
    <h3>DUIS AUTE IRURE</h3>
    <svg viewBox="0 0 34 40" width="34" fill="none" stroke="#444" stroke-width="2">
      <path d="M3 6l14-4 14 4v20l-14 12L3 26z"/>
      <path d="M10 13h14M10 19h14M10 25h10"/>
    </svg>
    <p>Excepteur sint occaecat cupi datat non it proident, sunt in culpa qui officia dese runtorn mollit anim id est laborum.</p>
  </article>

  <article class="service" style="left:397px">
    <h3>DUIS AUTE IRURE</h3>
    <svg viewBox="0 0 42 40" width="42" fill="none" stroke="#444" stroke-width="2">
      <path d="M8 20V2h26v18"/><path d="M13 8h16M13 13h16"/>
      <path d="M2 20h12v6h14v-6h12v18H2z"/>
    </svg>
    <p>Excepteur sint occaecat cupi datat non it proident, sunt in culpa qui officia dese runtorn mollit anim id est laborum.</p>
  </article>

  <article class="service" style="left:558px">
    <h3>DUIS AUTE IRURE</h3>
    <svg viewBox="0 0 50 40" width="50" fill="none" stroke="#444" stroke-width="2">
      <path d="M2 3h16l4 5h26v30H2z"/><path d="M2 12h46"/>
    </svg>
    <p>Excepteur sint occaecat cupi datat non it proident, sunt in culpa qui officia dese runtorn mollit anim id est laborum.</p>
  </article>
</section>

<nav class="social" aria-label="Social media links">
  <a style="left:275px" href="#" aria-label="Social network one"><span class="dot"></span></a>
  <a class="active" style="left:343px" href="#" aria-label="Social network two"><span class="dot"></span></a>
  <a class="white" style="left:411px" href="#" aria-label="Social network three"><span class="dot"></span></a>
  <a class="white" style="left:474px" href="#" aria-label="Social network four"><span class="dot"></span></a>
</nav>

<footer class="site-footer">
  <div class="footer-col" style="left:80px">
    <h4>Location</h4>
    <address>220 Harbour View Road<br>Perth, WA 6000<br><span class="muted">(08) 555-0192</span></address>
    <p class="map-line"><a class="map-link" href="#">see it in the map</a> &rarr;</p>
  </div>
  <div class="footer-col" style="left:242px">
    <h4>Company</h4>
    <ul><li>Our story</li><li>Mission</li><li>Journal</li><li>Careers</li></ul>
  </div>
  <div class="footer-col" style="left:404px">
    <h4>Support</h4>
    <ul><li>FAQ</li><li>Contact us</li><li>Policies</li></ul>
  </div>
  <div class="footer-col" style="left:567px">
    <h4>Verita.</h4>
    <p class="about-text">Sed do eiusmod tempor incididunt ut labore et dolore magna aliqua.</p>
  </div>
</footer>

</body>
</html>
```